CORE 303 fitness page promoting new gym in Dania beach, FL

The purpose of the website is to attract new members to our new fitness facility opening in Dania beach, Florida. The city lacks places for functional training so we want to target this market of adult/young adult fitness personal. Not just meant for fitness buffs, first timers are encouraged to begin their health/fitness journey with us. Family owned, providing a combination of fitness services include personal and small group strength training, large group fitness classes with the use of sleds, dumbbells, kettlebells, medicine balls, cones, hurdles, ladders, and punching bags. Smoothie bar inside as well. Need to deliver a clear message of what kind of workouts we do, the people we want to attract, and how to sign up. Also make it known that we have showers on site (very rare to find in fitness studios).
Target Market(s)
Fit, health conscious, business professionals
Industry/Entity Type
Fitness
Number of Pages Required
3 page
Requirements
Must have
- Bright colors that scream SIGN UP, Would like to see logo in large, a big attractive sign saying First class is free. The concept of the gym is that we educate our clients on fitness rather than throwing them blindly into working out. We want our layout to mimic a schools idea of having a curriculum (styles of class/schedule) a tuition (membership costs).
Nice to have
- Big images that promote the gym, option to have video on front page displaying workouts.

```html
<!DOCTYPE html>
<html lang="en">
<head>
<meta charset="utf-8">
<title>CORE 303 — Fitness</title>
<link rel="stylesheet" href="https://fonts.googleapis.com/css2?family=Lato:wght@400;700&family=Roboto:wght@400;500&display=swap">
<style>
  :root {
    --black: #000000;
    --orange: #ff5a1f;
    --white: #ffffff;
    --ink: #111111;
    --card-bg: #f4f4f4;
    --rule: #dddddd;
    --dark: #141414;
  }
  * { box-sizing: border-box; margin: 0; padding: 0; }
  html, body { width: 1093px; height: 1200px; overflow: hidden; background: var(--white); }
  body { position: relative; font-family: 'Lato', sans-serif; }

  .site-header {
    position: absolute; left: 0; top: 0; width: 1093px; height: 71px;
    background: var(--black);
  }
  .brand {
    position: absolute; left: 88px; top: 24px;
    display: flex; align-items: center; gap: 7px;
    color: var(--white); font-family: 'Lato', sans-serif; font-weight: 700; font-size: 18px;
  }
  .brand-dot { width: 10px; height: 10px; background: var(--orange); }
  .main-nav a {
    position: absolute; top: 29px; font-size: 13px; color: var(--white); text-decoration: none;
  }
  .main-nav a.active { color: var(--orange); }

  .hero {
    position: absolute; left: 0; top: 71px; width: 1093px; height: 569px;
    background: radial-gradient(ellipse at 40% 40%, #4a4a4a 0%, #2a2a2a 45%, #111 100%);
  }
  .hero-title {
    position: absolute; left: 0; width: 100%; top: 227px; text-align: center;
    font-weight: 700; font-size: 59px; color: var(--white); line-height: 1;
  }
  .hero-title .free { color: var(--orange); }
  .hero-sub {
    position: absolute; left: 0; width: 100%; top: 318px; text-align: center;
    font-weight: 700; font-size: 15px; color: var(--white);
  }
  .btn-register {
    position: absolute; left: 466px; top: 375px; width: 160px; height: 44px;
    border: 2px solid var(--orange); border-radius: 22px;
    color: var(--white); font-weight: 700; font-size: 16px;
    display: flex; align-items: center; justify-content: center;
  }

  .section-title {
    position: absolute; font-family: 'Roboto', sans-serif; font-weight: 400;
    font-size: 25px; text-transform: uppercase; line-height: 1;
  }
  .featured-title { left: 91px; top: 699px; color: var(--ink); }
  .featured-rule { position: absolute; left: 367px; top: 711px; width: 555px; height: 1px; background: var(--rule); }
  .carousel-btn {
    position: absolute; top: 700px; width: 26px; height: 26px; background: var(--orange);
    display: flex; align-items: center; justify-content: center;
  }

  .class-card { position: absolute; top: 783px; width: 293px; height: 207px; background: var(--card-bg); }
  .class-photo { width: 100%; height: 142px; }
  .class-name {
    position: absolute; left: 17px; top: 163px;
    font-family: 'Roboto', sans-serif; font-size: 17px; color: var(--ink);
  }

  .schedule {
    position: absolute; left: 0; top: 1049px; width: 1093px; height: 151px;
    background: linear-gradient(90deg, #2b2b2b 0%, var(--dark) 35%, #0d0d0d 100%);
  }
  .schedule-title { left: 85px; top: 79px; color: var(--white); font-weight: 500; }
  .schedule-rule { position: absolute; left: 85px; right: 85px; bottom: 1px; height: 1px; background: #444; }
</style>
</head>
<body>
  <header class="site-header">
    <div class="brand"><span class="brand-dot"></span>CORE 303</div>
    <nav class="main-nav">
      <a href="#" class="active" style="left:526px">NMB Schedule</a>
      <a href="#" style="left:650px">FTL Schedule</a>
      <a href="#" style="left:765px">Gallery</a>
      <a href="#" style="left:844px">Contact</a>
      <a href="#" style="left:928px">Personal Training</a>
    </nav>
  </header>

  <section class="hero" role="img" aria-label="Woman preparing to deadlift a loaded barbell in a gym, black and white photo">
    <h1 class="hero-title">First class is <span class="free">FREE!</span></h1>
    <p class="hero-sub">Ready to change your physique, but can’t work out in the gym?</p>
    <a class="btn-register">Register</a>
  </section>

  <h2 class="section-title featured-title">Featured Classes</h2>
  <div class="featured-rule"></div>
  <div class="carousel-btn" style="left:946px">
    <svg width="10" height="10" viewBox="0 0 10 10"><path d="M6.5 1.5 3 5l3.5 3.5" fill="none" stroke="#fff" stroke-width="1.6"/></svg>
  </div>
  <div class="carousel-btn" style="left:976px">
    <svg width="10" height="10" viewBox="0 0 10 10"><path d="M3.5 1.5 7 5 3.5 8.5" fill="none" stroke="#fff" stroke-width="1.6"/></svg>
  </div>

  <article class="class-card" style="left:90px">
    <div class="class-photo" role="img" aria-label="Two kettlebells on a gym floor with dumbbell rack behind" style="background:linear-gradient(135deg,#3a3a3a,#1c1c1c 60%,#5a5a5a)"></div>
    <span class="class-name">Power</span>
  </article>
  <article class="class-card" style="left:399px">
    <div class="class-photo" role="img" aria-label="Group bootcamp class with battle ropes in a bright studio" style="background:linear-gradient(135deg,#c9c9c9,#7d7f86 55%,#3d4150)"></div>
    <span class="class-name">Bootcamp</span>
  </article>
  <article class="class-card" style="left:709px">
    <div class="class-photo" role="img" aria-label="Boxing ring with blue canvas and hanging punching bags" style="background:linear-gradient(180deg,#6b5a55 0%,#3a2f2e 40%,#2f3f8a 75%,#222 100%)"></div>
    <span class="class-name">Boxing</span>
  </article>

  <section class="schedule" role="img" aria-label="Dark gym background photo of a woman training">
    <h2 class="section-title schedule-title">Class Schedule</h2>
    <div class="schedule-rule"></div>
  </section>
</body>
</html>
```